Visitenkarten-Design für Yogakurse
Zielgruppe
Ich biete Yogakurse für alle an sowieso speziell Yogakurse für Schwangere, frischgebackene Mamas und Rückbildungskurse.
Meine Zielgruppe sind hauptsächlich schwangere Frauen sowieso Frauen mit Babys.
Aufgabenstellung
Folgende Informationen sollten enthalten sein:
Ruhe im Atem
Yoga & Beckenbodentraining
Henrike Wolmsen
info@ruhe-im-atem-beispiel.de
www.ruhe-im-atem-beispiel.de

```html
<!DOCTYPE html>
<html lang="de">
<head>
<meta charset="utf-8">
<title>Ruhe im Atem – Visitenkarten</title>
<link rel="stylesheet" href="https://fonts.googleapis.com/css2?family=Nanum+Brush+Script&family=Manrope:wght@500;600;700&display=swap">
<style>
  :root {
    --page: #c8c8c8;
    --card: #e3e6dd;
    --brown: #b48e76;
    --green: #c4ddb4;
    --ink: #a98672;
    --crescent: #c7a893;
    --disc: #f5f6f2;
  }
  * { margin: 0; padding: 0; box-sizing: border-box; }
  html, body { width: 1200px; height: 800px; overflow: hidden; background: var(--page); }
  .stage { position: relative; width: 1200px; height: 800px; }
  .card {
    position: absolute; top: 245px; width: 540px; height: 310px;
    background: var(--card); overflow: hidden;
  }
  .card--front { left: 40px; }
  .card--back { left: 620px; }
  .card__art { position: absolute; inset: 0; }
  .brand-name {
    position: absolute; transform: translate(-50%, -50%);
    font-family: "Manrope", sans-serif; font-weight: 700;
    font-size: 20px; color: var(--ink); white-space: nowrap;
  }
  .tagline-script {
    position: absolute; left: 0; right: 0; top: 222px; text-align: center;
    font-family: "Nanum Brush Script", cursive; font-size: 44px; color: var(--ink);
  }
  .contact { position: absolute; left: 275px; top: 34px; }
  .contact__name {
    font-family: "Nanum Brush Script", cursive; font-size: 46px; line-height: 1;
    color: var(--ink); white-space: nowrap;
  }
  .contact__role {
    margin-top: 10px; font-family: "Manrope", sans-serif; font-weight: 700;
    font-size: 12.5px; letter-spacing: 0.04em; color: var(--ink);
  }
  .contact__list { list-style: none; margin-top: 22px; }
  .contact__item {
    display: flex; align-items: center; gap: 12px; height: 20px; margin-bottom: 17px;
    font-family: "Manrope", sans-serif; font-weight: 600; font-size: 11.5px; color: var(--ink);
  }
  .contact__item svg { width: 18px; height: 18px; flex: none; }
</style>
</head>
<body>
<div class="stage">

  <section class="card card--front">
    <svg class="card__art" viewBox="0 0 540 310" width="540" height="310">
      <polygon points="0,0 62,0 0,62" fill="var(--green)"/>
      <polygon points="0,0 42,0 0,42" fill="var(--brown)"/>
      <polygon points="540,310 470,310 540,240" fill="var(--green)"/>
      <polygon points="540,310 498,310 540,268" fill="var(--brown)"/>
      <circle cx="242" cy="130" r="83" fill="var(--crescent)" role="img" aria-label="Gestreifter Halbmond als Dekor"/>
      <circle cx="296" cy="130" r="82" fill="var(--disc)"/>
    </svg>
    <div class="brand-name" style="left:296px; top:130px;">Ruhe im Atem</div>
    <p class="tagline-script">Yoga &amp; Beckenbodentraining</p>
  </section>

  <section class="card card--back">
    <svg class="card__art" viewBox="0 0 540 310" width="540" height="310">
      <polygon points="0,0 62,0 0,62" fill="var(--green)"/>
      <polygon points="0,0 42,0 0,42" fill="var(--brown)"/>
      <polygon points="540,310 470,310 540,240" fill="var(--green)"/>
      <polygon points="540,310 498,310 540,268" fill="var(--brown)"/>
      <circle cx="128" cy="145" r="80" fill="var(--crescent)" role="img" aria-label="Gestreifter Halbmond als Dekor"/>
      <circle cx="176" cy="145" r="79" fill="var(--disc)"/>
      <line x1="262" y1="58" x2="262" y2="240" stroke="var(--ink)" stroke-width="1.5"/>
      <circle cx="262" cy="58" r="2.5" fill="var(--ink)"/>
      <circle cx="262" cy="240" r="2.5" fill="var(--ink)"/>
    </svg>
    <div class="brand-name" style="left:176px; top:145px;">Ruhe im Atem</div>

    <div class="contact">
      <h1 class="contact__name">Henrike Wolmsen</h1>
      <p class="contact__role">YOGA &amp; BECKENBODENTRAINING</p>
      <ul class="contact__list">
        <li class="contact__item">
          <svg viewBox="0 0 24 24" aria-hidden="true"><path d="M6 2h4l1.5 5-2.5 1.5a11 11 0 0 0 6.5 6.5L17 12.5l5 1.5v4a2 2 0 0 1-2 2A18 18 0 0 1 4 4a2 2 0 0 1 2-2z" fill="var(--ink)"/></svg>
          0170 - 4839215
        </li>
        <li class="contact__item">
          <svg viewBox="0 0 24 24" aria-hidden="true"><rect x="2" y="5" width="20" height="14" fill="none" stroke="var(--ink)" stroke-width="1.8"/><path d="M2 5l10 8 10-8" fill="none" stroke="var(--ink)" stroke-width="1.8"/></svg>
          info@ruhe-im-atem-beispiel.de
        </li>
        <li class="contact__item">
          <svg viewBox="0 0 24 24" aria-hidden="true" fill="none" stroke="var(--ink)" stroke-width="1.5"><circle cx="12" cy="12" r="10"/><ellipse cx="12" cy="12" rx="4.5" ry="10"/><path d="M2 12h20M4 7h16M4 17h16"/></svg>
          www.ruhe-im-atem-beispiel.de
        </li>
      </ul>
    </div>
  </section>

</div>
</body>
</html>
```